New homepage design www.quillharbor.nl

We need a new website design to go with our new designed logo.
We are a relativly small basketballclub that would like a shiny new webdesign for our homepage. We want te be able to create a real homepage/base for our clubmembers, where they can find news, upcoming events (agenda/calendar) and the related info on playing basketball at our club (games/tasks/teams and all).

The current website is located at: www.quillharbor.nl but is an outdated and not so appealing design.
There are no real designfeatures of the current site that have to be transferred to the new site.
Coding in HTML/CSS/JS/JPEG/PNG is enough, making a dynamic website will be my task. I just need the design in HTML (preferrably HTML 5)

There is not a huge budget, we are a club without a main sponsor.

Feel free to be creative and amaze us!

Text for the page in the new design will be created by us, you may use some sample text for filling.

Currently used pictures in the site don't have to be transferred to the new page (preferrably not!)
Updates

Tomorrow we will pick a design.

Industry/Entity Type

Events

Requirements
Must have
• The new logo as uploaded and attached.
News page.
Agenda page
HTML compatible same look and feel in all modern browsers (IE, FireFox, Chrome, Safari)
Nice to have
• HTML 5 validated and approved

```html
<!DOCTYPE html>
<html lang="nl">
<head>
<meta charset="utf-8">
<title>BC Quillharbor – Home</title>
<link href="https://fonts.googleapis.com/css2?family=Oswald:wght@400;500;600&family=Open+Sans:wght@400;700&display=swap" rel="stylesheet">
<style>
:root{
  --navy:#21364e;
  --orange:#f28c2c;
  --grey:#747474;
  --grey-text:#777;
  --band-text:#dfe4ea;
  --white:#fff;
}
*{margin:0;padding:0;box-sizing:border-box}
html,body{width:1200px;height:1046px;overflow:hidden;background:var(--white)}
body{position:relative;font-family:"Open Sans",sans-serif}
.hero{position:absolute;left:0;top:0;width:1200px;height:464px;background:linear-gradient(#ececec,#cdcdcd)}
.player{position:absolute;left:515px;top:0;width:500px;height:456px;background:linear-gradient(160deg,#f08a24 0%,#f08a24 30%,#233a54 45%,#eeeeee 65%,#c8102e 100%);opacity:.85;border-radius:40px 40px 80px 120px}
.brand{position:absolute;left:148px;top:82px;display:flex;align-items:center;gap:8px;font-family:"Oswald",sans-serif;font-weight:600;font-size:20px;line-height:24px;color:var(--navy)}
.brand .dot{width:24px;height:24px;border-radius:50%;background:var(--orange);flex:none}
.nav{position:absolute;left:324px;top:60px;width:747px;height:46px;background:var(--navy);border-bottom:4px solid #8a8a8a;display:flex;list-style:none}
.nav li{font-family:"Oswald",sans-serif;font-size:20px;color:#d6dbe1;line-height:42px;padding:0 14px}
.nav li.active{background:var(--grey);color:var(--white);padding:0 14px 0 22px}
.welcome{position:absolute;left:155px;top:200px;font-family:"Oswald",sans-serif;font-weight:600;font-size:60px;line-height:90px;color:var(--navy);letter-spacing:-1px}
.tagline{position:absolute;left:157px;top:287px;font-family:"Oswald",sans-serif;font-weight:500;font-size:37px;line-height:44px;color:var(--grey-text);letter-spacing:-1px}
.tagline em{font-style:normal;color:var(--orange)}
.notice{position:absolute;left:0;top:464px;width:1200px;height:134px;background:var(--navy);padding:21px 148px 0 117px;font-size:14.3px;line-height:17px;color:var(--band-text)}
.notice strong{color:var(--white)}
.announce{position:absolute;left:118px;top:619px;width:452px;height:319px;background:var(--orange);padding:16px 34px 0 12px;color:var(--white)}
.announce h2{font-family:"Oswald",sans-serif;font-weight:500;font-size:25px;line-height:34px;margin-bottom:14px}
.announce p{font-size:12px;line-height:14.5px}
.announce ul{margin:10px 0 0 14px;font-size:12px;line-height:14.5px;list-style:none}
.announce li::before{content:"";display:inline-block;width:6px;height:6px;border-radius:50%;background:var(--white);margin:0 8px 1px -14px}
.read-more{position:absolute;left:13px;bottom:18px;font-family:"Oswald",sans-serif;font-weight:500;font-size:19px}
.teams{position:absolute;left:580px;top:619px;width:500px;height:173px;background:var(--grey);padding:8px 17px;color:var(--white)}
.teams h2{font-family:"Oswald",sans-serif;font-weight:500;font-size:26px;line-height:34px;color:#e4e4e4}
.team-cols{display:flex;gap:42px;margin-top:2px}
.team-cols ul{list-style:none;width:209px}
.team-cols li{font-size:12px;line-height:22px;border-bottom:1px solid #c9c9c9;padding-left:1px;height:23px}
.gallery-title{position:absolute;left:583px;top:800px;font-family:"Oswald",sans-serif;font-weight:500;font-size:31px;line-height:44px;color:var(--grey)}
.gallery-more{position:absolute;left:1038px;top:812px;font-family:"Oswald",sans-serif;font-size:19px;color:#888}
.thumb{position:absolute;top:843px;height:95px;border:3px solid #c6c6c6;background:linear-gradient(#8d8d8d,#3f63b4 60%,#c3a46a)}
.footer{position:absolute;left:0;top:964px;width:1200px;border-top:2px solid #d4d4d4}
.foot-nav{position:absolute;left:118px;top:984px;display:flex;gap:13px;list-style:none;font-family:Arial,sans-serif;font-size:12.5px;color:#555}
.copyright{position:absolute;left:118px;top:1004px;font-family:Arial,sans-serif;font-size:11px;color:#888}
.social{position:absolute;top:989px;width:28px;height:28px;border-radius:50%;background:#a8a8a8}
.foot-brand{position:absolute;left:1000px;top:996px;font-family:"Open Sans",sans-serif;font-weight:700;font-size:11px;color:#9a9a9a}
</style>
</head>
<body>
<header class="hero">
  <div class="player" role="img" aria-label="Illustration of a basketball player in orange shorts and red shoes leaping"></div>
  <div class="brand"><span class="dot"></span>QUILLHARBOR</div>
  <ul class="nav">
    <li class="active">HOME</li><li>TEAMS</li><li>INFORMATION</li><li>GALLERY</li><li>CONTACT</li><li>LINKS</li><li>GUESTBOOK</li><li>LOGIN</li>
  </ul>
  <h1 class="welcome">WELKOM</h1>
  <p class="tagline">Het bestuur van BC<br><em>Quillharbor</em> heet je<br>welkom op onze site.</p>
</header>

<section class="notice">
  <strong>CLOTHING:</strong> If you do not yet have complete basketball clothes, think of Ember Hoops. Quillharbor is going to work. These sports in Veldmere together This sporting goods store has all the necessary stuff for basketball. Think of shoes, a dress or suits. The choice is well represented, and there is also a nice discount on! So if you need new stuff, then just walk in Ember Hoops in Veldmere inside. Indicate that you are a member of Quillharbor and the discount will be deducted. Of all purchases from members of Quillharbor association gets as a small amount. This will be invested in new materials. Thus, our association members both helped!
</section>

<section class="announce">
  <h2>IMPORTANT ANNOUNCEMENTS:</h2>
  <p>IMPORTANT DATES: throughout the season, there are a few dates that we are unfortunately not able to make use of the sports hall or gymnasium Ravenhof use. Ther are also a number of important other data. Consider the transition from the Tuesday of the sports hall to hall Ravenhof (and back again). Below is a summary of these important dates:</p>
  <ul>
    <li>31-12-2013 No training related New Year's Eve</li>
    <li>20-02-2014 No training related carnival</li>
    <li>24-02-2014 No training related carnival</li>
    <li>25-02-2014 No training related carnival</li>
    <li>27-02-2014 No training related carnival</li>
    <li>03-03-2014 No training related carnival</li>
    <li>04-03-2014 No training related carnival</li>
  </ul>
  <span class="read-more">READ MORE +</span>
</section>

<section class="teams">
  <h2>TEAMS</h2>
  <div class="team-cols">
    <ul><li>01. Ladies Recreaten 1</li><li>02. Seneor Women 1</li><li>03. Externals</li><li>04. Recereaten Men</li><li>05. Seneor Men 1</li></ul>
    <ul><li>Ladies Recreaten 1</li><li>Seneor Women 1</li><li>Externals</li><li>Recereaten Men</li><li>Seneor Men 1</li></ul>
  </div>
</section>

<h2 class="gallery-title">GALLERY</h2>
<span class="gallery-more">MORE</span>
<div class="thumb" style="left:584px;width:143px" role="img" aria-label="Team photo of players in blue kit in a sports hall"></div>
<div class="thumb" style="left:737px;width:127px" role="img" aria-label="Players sitting on a sports hall floor"></div>
<div class="thumb" style="left:875px;width:96px" role="img" aria-label="Team photo of players in blue kit"></div>
<div class="thumb" style="left:982px;width:99px" role="img" aria-label="Players resting in the gymnasium"></div>

<footer class="footer"></footer>
<ul class="foot-nav"><li>HOME</li><li>TEAMS</li><li>INFORMATION</li><li>GALLERY</li><li>CONTACT</li><li>LINKS</li><li>GUESTBOOK</li><li>LOGIN</li></ul>
<p class="copyright">© Copyright 2002 - 2013 Company Name. All Rights Reserved</p>
<span class="social" style="left:808px" aria-label="Social link"></span>
<span class="social" style="left:844px" aria-label="Social link"></span>
<span class="social" style="left:881px" aria-label="Social link"></span>
<span class="foot-brand">QUILLHARBOR</span>
</body>
</html>
```